Brightwell Systems, a software development company, needs a website

We need a website to promote our software development company. The company is brand new and we want to market ourselves. We develop all kinds of software from web applications, to desktop applications, to mobile applications. Small company, not a lot of history, just need something flashy.

```html
<!DOCTYPE html>
<html lang="en">
<head>
<meta charset="utf-8">
<title>Brightwell Systems — Software Development</title>
<link href="https://fonts.googleapis.com/css2?family=Montserrat:ital,wght@0,400;0,500;0,600;0,700;1,400;1,500&display=swap" rel="stylesheet">
<style>
:root{
  --bg:#f5f7fd;
  --band:#eef1fb;
  --white:#ffffff;
  --blue:#2b5fe0;
  --blue-soft:#dde4fa;
  --wave1:#d6ddf8;
  --wave2:#c3cdf4;
  --ink:#1f2440;
  --text:#5d6275;
  --muted:#9a9fb0;
  --line:#e2e5ee;
  --star:#f0b400;
}
*{box-sizing:border-box;margin:0;padding:0}
html,body{width:1200px;height:3773px;overflow:hidden}
body{background:var(--bg);font-family:'Montserrat',sans-serif;color:var(--ink);position:relative}
.abs{position:absolute}
a{color:inherit;text-decoration:none}

/* header */
.logo{display:flex;align-items:center;gap:6px;font-size:20px;font-weight:500;color:var(--ink)}
.logo-dot{width:34px;height:34px;border:3px solid var(--blue);border-radius:50%}
.site-header .logo{left:161px;top:26px}
.nav{left:593px;top:30px;display:flex;gap:0;font-size:13px;color:var(--ink)}
.nav a{position:absolute;white-space:nowrap}
.sign-in{left:940px;top:19px;width:97px;height:35px;border:2px solid var(--blue);border-radius:18px;color:var(--blue);font-size:13px;display:flex;align-items:center;justify-content:center}

/* hero */
.hero-title{left:161px;top:180px;font-size:32px;font-weight:600;line-height:54px;color:var(--ink)}
.hero-text{left:161px;top:296px;width:400px;font-size:13px;line-height:23px;color:var(--ink)}
.btn{background:var(--blue);color:var(--white);border-radius:20px;display:flex;align-items:center;justify-content:center;font-weight:600;box-shadow:0 8px 18px rgba(43,95,224,.3)}
.hero-btn{left:161px;top:363px;width:151px;height:35px;font-size:11px;letter-spacing:1px}
.hero-art{left:690px;top:95px;width:300px;height:390px;border-radius:150px 150px 40px 40px;background:linear-gradient(180deg,#e6ebfb,#c9d3f3)}

/* section headings */
.eyebrow{left:0;width:1200px;text-align:center;font-size:11px;font-weight:600;letter-spacing:1px;color:var(--blue)}
.section-title{left:0;width:1200px;text-align:center;font-size:32px;font-weight:500;color:var(--ink)}

/* services */
.service{width:240px;text-align:center}
.service-icon{width:46px;height:46px;margin:0 auto;background:var(--white);border-radius:6px;box-shadow:0 4px 14px rgba(31,36,64,.08);display:flex;align-items:center;justify-content:center}
.service h3{margin-top:18px;font-size:14px;font-weight:600;line-height:21px}
.service p{margin-top:12px;font-size:12px;line-height:21px;color:var(--text)}
.read-more{font-size:12px;font-style:italic;color:var(--blue);display:block}
.service .read-more{margin-top:12px}
.divider{left:161px;width:876px;height:1px;background:var(--line)}

/* project */
.blob{left:161px;top:1333px;width:381px;height:425px;background:#eaeefa;border-radius:55% 45% 50% 50%/45% 50% 50% 55%}
.phone{left:283px;top:1316px;width:196px;height:395px;background:#15151c;border-radius:28px;padding:10px;box-shadow:20px 20px 40px rgba(31,36,64,.15)}
.phone-screen{width:100%;height:100%;border-radius:20px;background:linear-gradient(160deg,#3a6cf0,#2554d6);display:flex;flex-direction:column;align-items:center;justify-content:center;color:var(--white);font-size:17px;font-weight:600;gap:20px;position:relative}
.phone-notch{position:absolute;top:0;left:50%;transform:translateX(-50%);width:90px;height:16px;background:#15151c;border-radius:0 0 12px 12px}
.project{left:612px;top:1390px;width:400px}
.project h3{font-size:18px;font-weight:600;color:var(--blue)}
.project p{margin-top:14px;font-size:12.5px;line-height:25.5px;color:var(--text)}
.project .read-more{margin-top:14px}

/* testimonials */
.client-band{left:0;top:1790px;width:1200px;height:620px;background:var(--band)}
.review{width:277px;height:285px;padding:18px 22px;border-bottom:1px solid var(--line)}
.review.featured{background:var(--white);border-bottom:none;box-shadow:0 6px 24px rgba(31,36,64,.08)}
.reviewer{display:flex;gap:16px;align-items:center}
.avatar{width:36px;height:36px;border-radius:50%;background:linear-gradient(135deg,#d9b59a,#8b6a55)}
.reviewer b{display:block;font-size:13px;font-weight:600}
.reviewer span{font-size:11px;color:var(--muted)}
.review p{margin-top:22px;font-size:12px;line-height:23px;color:var(--text)}
.stars{position:absolute;left:22px;top:245px;color:var(--star);font-size:14px;letter-spacing:1px}

/* contact */
.contact-title{left:0;width:1200px;text-align:center;font-size:31px;font-weight:500;line-height:48px}
.contact-card{left:163px;top:2675px;width:874px;height:478px;background:var(--white);box-shadow:0 4px 20px rgba(31,36,64,.06)}
.map{left:4px;top:4px;width:416px;height:470px;background:linear-gradient(135deg,#e4e4e4,#cfcfcf)}
.map-pin{left:106px;top:175px;width:208px;height:108px;background:var(--white);border-radius:4px;box-shadow:0 4px 14px rgba(0,0,0,.15);padding:18px 16px;font-size:11px;line-height:16px;color:var(--ink)}
.map-pin div{display:flex;gap:8px;margin-bottom:12px}
.field{left:489px;width:316px;height:37px;border:1px solid var(--line);border-radius:19px;font-size:11px;color:var(--muted);padding:11px 17px}
.field.message{height:115px;border-radius:8px}
.submit{left:489px;top:378px;width:316px;height:38px;font-size:14px;letter-spacing:.5px}

/* footer */
.site-footer .logo{left:159px;top:3466px}
.footer-about{left:163px;top:3520px;width:230px;font-size:11.5px;line-height:20px;color:var(--text)}
.footer-col{top:3470px}
.footer-col h4{font-size:16px;font-weight:700;letter-spacing:1px;margin-bottom:14px}
.footer-col li{list-style:none;font-size:11.5px;line-height:28px;color:var(--text);display:flex;align-items:center;gap:10px}
.social-dot{width:12px;height:12px;border-radius:50%;background:var(--blue)}
.copyright{left:0;top:3738px;width:1200px;text-align:center;font-size:11px;color:var(--text)}
</style>
</head>
<body>

<header class="site-header">
  <a class="logo abs" href="#"><span class="logo-dot"></span>Brightwell Systems</a>
  <nav class="nav abs">
    <a href="#" style="left:0">Home</a>
    <a href="#" style="left:88px">About</a>
    <a href="#" style="left:169px">Services</a>
    <a href="#" style="left:267px">Contact</a>
  </nav>
  <a class="sign-in abs" href="#">Sign in</a>
</header>

<section class="hero">
  <h1 class="hero-title abs">Mobile App, Web,<br>API, IoT &amp; Development</h1>
  <p class="hero-text abs">Morbi accumsan ipsum velit. Nam nec tellus a odio tincidunt auctor a ornare odio.</p>
  <a class="btn hero-btn abs" href="#">GET IN TOUCH</a>
  <div class="hero-art abs" role="img" aria-label="Illustration of a developer working on a laptop with floating code icons"></div>
  <svg class="abs" style="left:0;top:505px" width="1200" height="130" viewBox="0 0 1200 130">
    <path d="M0 85 C200 20 420 20 640 60 C850 100 1000 40 1200 60 L1200 130 L0 130Z" fill="var(--wave1)" opacity=".7"/>
    <path d="M300 100 C550 30 800 30 1000 80 C1100 100 1150 90 1200 85 L1200 130 L300 130Z" fill="var(--wave2)" opacity=".5"/>
    <path d="M0 95 C300 60 500 120 800 110 C1000 100 1100 110 1200 100 L1200 130 L0 130Z" fill="var(--bg)"/>
  </svg>
</section>

<section class="services">
  <p class="eyebrow abs" style="top:718px">WHAT WE DO</p>
  <h2 class="section-title abs" style="top:748px">Services We Offer</h2>

  <article class="service abs" style="left:180px;top:844px">
    <div class="service-icon"><svg width="26" height="26" viewBox="0 0 26 26" fill="none" stroke="#3bb3a8" stroke-width="1.5"><rect x="3" y="3" width="20" height="14" rx="1"/><path d="M10 8l-2 2 2 2M16 8l2 2-2 2M9 21h8M13 17v4"/></svg></div>
    <h3>Web / API<br>Developement</h3>
    <p>Aenean sollicitudin, lorem quis bibendum auctor, nisi elit consequat ipsum, nec sagittis sem.</p>
    <a class="read-more" href="#">Read More &gt;</a>
  </article>

  <article class="service abs" style="left:479px;top:844px">
    <div class="service-icon"><svg width="26" height="26" viewBox="0 0 26 26" fill="none" stroke="#ef5a6f" stroke-width="1.5"><rect x="7" y="2" width="12" height="22" rx="2"/><circle cx="13" cy="20" r="1"/><circle cx="12" cy="12" r="2"/><circle cx="16" cy="9" r="1.5"/></svg></div>
    <h3>Mobile App<br>Developement</h3>
    <p>Aenean sollicitudin, lorem quis bibendum auctor, nisi elit consequat ipsum, nec sagittis sem.</p>
    <a class="read-more" href="#">Read More &gt;</a>
  </article>

  <article class="service abs" style="left:778px;top:844px">
    <div class="service-icon"><svg width="28" height="26" viewBox="0 0 28 26" fill="none" stroke="var(--blue)" stroke-width="1.6" stroke-linecap="round"><path d="M3 10a16 16 0 0 1 22 0M7 14a10 10 0 0 1 14 0M11 18a4 4 0 0 1 6 0"/><circle cx="14" cy="21" r="1.2" fill="var(--blue)"/></svg></div>
    <h3>Internet of<br>Things</h3>
    <p>Aenean sollicitudin, lorem quis bibendum auctor, nisi elit consequat ipsum, nec sagittis sem.</p>
    <a class="read-more" href="#">Read More &gt;</a>
  </article>

  <div class="divider abs" style="top:1146px"></div>
</section>

<section class="works">
  <p class="eyebrow abs" style="top:1203px">OUR WORKS</p>
  <h2 class="section-title abs" style="top:1232px">Latest Projects</h2>
  <div class="blob abs"></div>
  <div class="phone abs">
    <div class="phone-screen" role="img" aria-label="App splash screen with a person photo in blue tint">
      <span class="phone-notch"></span>
      <svg width="60" height="60" viewBox="0 0 60 60"><circle cx="30" cy="30" r="22" fill="none" stroke="#fff" stroke-width="4"/></svg>
      <span>Brightwell Systems</span>
    </div>
  </div>
  <div class="project abs">
    <h3>Mobile App Developement</h3>
    <p>Duis sed odio sit amet nibh vulputate cursus a sit amet mauris. Morbi accumsan ipsum velit. Nam nec tellus a odio tincidunt auctor a ornare odio. Sed non mauris vitae erat consequat auctor eu in elit. Class aptent taciti sociosqu ad litora torquent per conubia nostra, per inceptos himenaeos.</p>
    <a class="read-more" href="#">Read More &gt;</a>
  </div>
</section>

<section class="clients">
  <div class="client-band abs"></div>
  <svg class="abs" style="left:0;top:1728px" width="1200" height="100" viewBox="0 0 1200 100">
    <path d="M0 12 C200 0 420 100 650 80 C850 60 1000 20 1200 40 L1200 100 L0 100Z" fill="var(--band)"/>
  </svg>
  <svg class="abs" style="left:0;top:2340px" width="1200" height="100" viewBox="0 0 1200 100">
    <path d="M0 10 C250 60 500 0 750 0 C950 0 1050 30 1200 30 L1200 0 L0 0Z" fill="var(--band)"/>
    <path d="M0 10 C250 60 500 0 750 0 C950 0 1050 30 1200 30 L1200 100 L0 100Z" fill="var(--bg)"/>
  </svg>
  <p class="eyebrow abs" style="top:1879px">OUR CLIENTS</p>
  <h2 class="section-title abs" style="top:1908px">What They Say</h2>

  <article class="review abs" style="left:161px;top:2000px">
    <div class="reviewer"><span class="avatar" role="img" aria-label="Client portrait"></span><div><b>Marta, USA</b><span>Northfield College</span></div></div>
    <p>Duis sed odio sit amet nibh vulputate cursus a sit amet mauris. Morbi accumsan ipsum velit. Nam nec tellus a odio tincidunt auctor a ornare odio. Sed non mauris vitae erat consequat auctor eu in elit.</p>
    <span class="stars">★★★★★</span>
  </article>
  <article class="review abs" style="left:461px;top:2000px">
    <div class="reviewer"><span class="avatar" role="img" aria-label="Client portrait"></span><div><b>Lena, EU</b><span>Owner, Maple &amp; Finch LLC</span></div></div>
    <p>Proin gravida nibh vel velit auctor aliquet. Aenean sollicitudin, lorem quis bibendum auctor, nisi elit consequat ipsum, nec sagittis sem nibh id elit.</p>
    <span class="stars">★★★★★</span>
  </article>
  <article class="review featured abs" style="left:760px;top:2000px">
    <div class="reviewer"><span class="avatar" role="img" aria-label="Client portrait"></span><div><b>Rosa, NY</b><span>CEO, Orbitline</span></div></div>
    <p>Duis sed odio sit amet nibh vulputate cursus a sit amet mauris. Morbi accumsan ipsum velit. Nam nec tellus a odio tincidunt auctor a ornare odio. Sed non mauris vitae erat consequat auctor eu in elit.</p>
    <span class="stars">★★★★★</span>
  </article>
</section>

<section class="contact">
  <p class="eyebrow abs" style="top:2506px">CONTACT US</p>
  <h2 class="contact-title abs" style="top:2533px">What are you waiting for ?<br>Let’s get on touch now</h2>
  <div class="contact-card abs">
    <div class="map abs" role="img" aria-label="City street map showing the office location">
      <div class="map-pin abs">
        <div><svg width="12" height="16" viewBox="0 0 12 16"><path d="M6 0a6 6 0 0 0-6 6c0 4 6 10 6 10s6-6 6-10a6 6 0 0 0-6-6z" fill="var(--blue)"/><circle cx="6" cy="6" r="2" fill="#fff"/></svg><span>48 Harbor Lane, Suite 2<br>Riverside</span></div>
        <div><svg width="13" height="13" viewBox="0 0 24 24"><path d="M6.6 10.8a15 15 0 0 0 6.6 6.6l2.2-2.2a1 1 0 0 1 1-.25 11 11 0 0 0 3.6.6 1 1 0 0 1 1 1V20a1 1 0 0 1-1 1A17 17 0 0 1 3 4a1 1 0 0 1 1-1h3.5a1 1 0 0 1 1 1 11 11 0 0 0 .6 3.6 1 1 0 0 1-.25 1z" fill="var(--blue)"/></svg><span>555-0142-780</span></div>
      </div>
    </div>
    <div class="field abs" style="top:57px">Name :</div>
    <div class="field abs" style="top:111px">Email :</div>
    <div class="field abs" style="top:164px">Phone :</div>
    <div class="field message abs" style="top:218px">Message :</div>
    <a class="btn submit abs" href="#">SUBMIT</a>
  </div>
</section>

<footer class="site-footer">
  <svg class="abs" style="left:0;top:3260px" width="1200" height="150" viewBox="0 0 1200 150">
    <path d="M0 50 C250 0 450 20 700 60 C900 90 1050 30 1200 50 L1200 150 L0 150Z" fill="var(--wave1)" opacity=".7"/>
    <path d="M200 60 C450 10 700 30 950 80 C1050 100 1150 90 1200 80 L1200 150 L200 150Z" fill="var(--wave2)" opacity=".5"/>
    <path d="M0 70 C300 120 550 60 800 110 C1000 140 1100 120 1200 115 L1200 150 L0 150Z" fill="var(--bg)"/>
  </svg>
  <a class="logo abs" href="#"><span class="logo-dot"></span>Brightwell Systems</a>
  <p class="footer-about abs">Aenean sollicitudin, lorem quis bibendum auctor, nisi elit consequat ipsum, nec sagittis sem nibh id elit. Duis sed odio sit amet nibh vulputate cursus.</p>
  <div class="footer-col abs" style="left:463px">
    <h4>SERVICES</h4>
    <ul><li>Workshops</li><li>Internet of Things</li><li>Ux and Ui</li><li>Development</li><li>Implementation</li></ul>
  </div>
  <div class="footer-col abs" style="left:687px">
    <h4>QUICK LINKS</h4>
    <ul><li>About</li><li>Services</li><li>Pricing</li><li>Blog</li><li>Contact</li></ul>
  </div>
  <div class="footer-col abs" style="left:914px">
    <h4>FOLLOW US</h4>
    <ul><li><span class="social-dot"></span>Friendloop</li><li><span class="social-dot"></span>Chirpline</li><li><span class="social-dot"></span>Snapframe</li><li><span class="social-dot"></span>Worknet</li></ul>
  </div>
  <div class="divider abs" style="top:3717px"></div>
  <p class="copyright abs">© Copyright 2019 Brightwell Systems. All Rights Reserved</p>
</footer>

</body>
</html>
```